Ferncrest Dental, LLC business card project

Business card to be designed with current logo.
Dental office- please keep design of card that looks clean and professional.
Please include the following info:
Ferncrest Dental, LLC
Dr. Lorna Pettigrew
2871 Marlowe Street
Bethlehem, PA 18093
610-555-0193
ferncrestdental.office@examplemail.test
Hello everyone-
Reason: Just got back from overseas- will look at all designs and provide feedback. Thank you!
Reason: Polling my friends for the final selection-
thank you to all those that participated- so many talented designers!

```html
<!DOCTYPE html>
<html lang="en">
<head>
<meta charset="utf-8">
<title>Ferncrest Dental, LLC — Business Card</title>
<link href="https://fonts.googleapis.com/css2?family=Open+Sans:wght@400;700&family=Quicksand:wght@400&display=swap" rel="stylesheet">
<style>
  :root {
    --page-bg: #b9b9b9;
    --card-green: #63a240;
    --accent-line: #a8c83a;
    --brand-green: #6aa637;
    --decor-light: rgba(190, 220, 150, 0.55);
    --decor-mid: rgba(150, 200, 90, 0.35);
    --card-white: #ffffff;
    --text-light: #ffffff;
  }
  * { box-sizing: border-box; margin: 0; padding: 0; }
  html, body {
    width: 1200px; height: 960px; overflow: hidden;
    background: var(--page-bg);
    font-family: "Open Sans", sans-serif;
  }
  .card {
    position: absolute;
    left: 320px;
    width: 575px;
    height: 379px;
    overflow: hidden;
    background: var(--card-green);
    box-shadow: 0 2px 6px rgba(0, 0, 0, 0.25);
  }
  .card--front { top: 97px; }
  .card--back { top: 512px; }

  .decor-area {
    position: absolute;
    background:
      radial-gradient(ellipse 38% 55% at 62% 42%, var(--decor-light), transparent 70%),
      radial-gradient(ellipse 70% 28% at 50% 100%, var(--decor-mid), transparent 75%);
  }
  .card--front .decor-area { left: 262px; top: 150px; width: 313px; height: 229px; }
  .card--back .decor-area { left: 360px; top: 232px; width: 215px; height: 147px; }

  .brand-name {
    position: absolute;
    font-family: "Quicksand", sans-serif;
    font-weight: 400;
    white-space: nowrap;
    display: flex;
    align-items: center;
    line-height: 1;
  }
  .brand-dot {
    display: inline-block;
    border-radius: 50%;
    flex: none;
  }
  .card--front .brand-name {
    left: 148px; top: 166px;
    gap: 8px;
    font-size: 25px;
    color: var(--text-light);
  }
  .card--front .brand-dot { width: 14px; height: 14px; background: var(--text-light); }

  .back-header {
    position: absolute; left: 0; top: 0;
    width: 100%; height: 170px;
    background: var(--card-white);
    border-bottom: 6px solid var(--accent-line);
  }
  .card--back .brand-name {
    left: 80px; top: 64px;
    gap: 10px;
    font-size: 38px;
    color: var(--brand-green);
  }
  .card--back .brand-dot { width: 20px; height: 20px; background: var(--brand-green); }

  .doctor-name {
    position: absolute;
    right: 55px; top: 194px;
    font-size: 20px; font-weight: 700;
    color: var(--text-light);
  }
  .contact {
    position: absolute;
    left: 56px; top: 236px;
    color: var(--text-light);
    font-size: 15px;
    font-style: normal;
    line-height: 19px;
  }
  .contact__company { font-weight: 700; font-size: 17px; margin-bottom: 4px; }
  .contact__row { display: flex; align-items: flex-start; gap: 6px; }
  .contact__icon { width: 12px; height: 19px; flex: none; fill: var(--text-light); }
  .contact__indent { padding-left: 18px; }
</style>
</head>
<body>
  <section class="card card--front">
    <div class="decor-area" role="img" aria-label="Soft decorative brand scene with trees and a rolling hill"></div>
    <div class="brand-name"><span class="brand-dot"></span>Ferncrest Dental, LLC</div>
  </section>

  <section class="card card--back">
    <div class="back-header">
      <div class="brand-name"><span class="brand-dot"></span>Ferncrest Dental, LLC</div>
    </div>
    <div class="decor-area" role="img" aria-label="Soft decorative brand scene with trees and a rolling hill"></div>
    <div class="doctor-name">Dr. Lorna Pettigrew</div>
    <address class="contact">
      <div class="contact__company">Ferncrest Dental, LLC</div>
      <div class="contact__row">
        <svg class="contact__icon" viewBox="0 0 12 19" aria-hidden="true"><path d="M6 4 L0.5 9 H2 V14 H5 V11 H7 V14 H10 V9 H11.5 Z"/></svg>
        <span>2871 Marlowe Street</span>
      </div>
      <div class="contact__indent">Bethlehem, PA 18093</div>
      <div class="contact__row">
        <svg class="contact__icon" viewBox="0 0 12 19" aria-hidden="true"><path d="M3 5 C2 5 1 6 1.3 8 C2 11 5 14.5 8 15 C9.5 15.3 10.5 14.5 10.8 13.5 L8.5 11.8 L7.3 12.8 C5.8 12 4.3 10.3 3.7 8.8 L4.8 7.8 Z"/></svg>
        <span>610-555-0193</span>
      </div>
      <div class="contact__row">
        <svg class="contact__icon" viewBox="0 0 12 19" aria-hidden="true"><path d="M0.5 6.5 H11.5 V14.5 H0.5 Z M0.5 6.5 L6 10.8 L11.5 6.5" stroke="#63a240" stroke-width="0.9"/></svg>
        <span>ferncrestdental.office@examplemail.test</span>
      </div>
    </address>
  </section>
</body>
</html>
```